Bright Pathway! A website showcasing who I am as a person

Bright Pathway started out as idea for me to better myself as a person and work on small projects that would help me grow as a person. Now I want to build a website showcasing "Bright Pathway." I want the website to showcase who I am and how I have grown both professionally and personally. I can build the raw code of the website on my own but I am not really much of a designer. I am looking for a design where I can write and post blogs, articles and share my thoughts. A little about myself and the ideas and interests that I want to share
What is Bright Pathway
Who I am
Background - Professional
Brand Marketing
Email Automation
Hiking
Rock Climbing
Traveling
Exercising and Transformation
"Personal Thoughts"
Hopefully this is enough information to get people started on some designs.
Work
3 page

```html
<!DOCTYPE html>
<html lang="en">
<head>
<meta charset="utf-8">
<title>Arin Castell — Bright Pathway</title>
<link href="https://fonts.googleapis.com/css2?family=Raleway:wght@400;500;600;700;800&display=swap" rel="stylesheet">
<style>
:root{
  --blue:#2f6db5;
  --blue-dark:#245a98;
  --ink:#2b2b2b;
  --text:#555a60;
  --muted:#8a8f96;
  --band:#eef0f2;
  --card:#f6f7f8;
  --menu:rgba(22,22,24,.92);
  --white:#ffffff;
}
*{box-sizing:border-box;margin:0;padding:0}
html,body{width:1200px;height:2584px;overflow:hidden}
body{font-family:"Raleway",sans-serif;color:var(--text);background:var(--white);position:relative}
.hero{position:absolute;left:0;top:0;width:1200px;height:600px;background:linear-gradient(120deg,#5a3f33 0%,#8d6a55 35%,#b89478 55%,#6d5346 80%,#3b2c26 100%)}
.topbar{position:absolute;left:0;top:0;width:1200px;height:64px;background:rgba(20,20,22,.85);display:flex;align-items:center;justify-content:space-between;padding:0 40px 0 36px}
.brand{color:var(--white);font-weight:700;font-size:26px;letter-spacing:1px}
.burger{width:30px;height:22px;display:flex;flex-direction:column;justify-content:space-between}
.burger span{height:3px;background:var(--white);border-radius:2px}
.hero-copy{position:absolute;left:320px;top:236px;width:600px;color:var(--white)}
.hero-copy h1{font-size:52px;font-weight:800;letter-spacing:1px;white-space:nowrap}
.hero-copy p{font-size:36px;line-height:44px;font-weight:500;margin-top:6px}
.dots{position:absolute;left:564px;top:552px;display:flex;gap:10px}
.dots i{width:12px;height:12px;border-radius:50%;background:rgba(255,255,255,.55)}
.dots i.on{background:var(--white)}
.menu{position:absolute;left:812px;top:72px;width:388px;height:720px;background:var(--menu);padding:52px 28px 0 32px;list-style:none;z-index:3}
.menu li{color:var(--white);font-size:17px;font-weight:600;height:60px;display:flex;align-items:flex-start;gap:14px;letter-spacing:.5px}
.menu li::before{content:"›";color:#bbb;font-size:18px;line-height:20px}
.menu small{display:block;font-size:15px;font-weight:500;color:#cfcfcf;margin-top:4px}
.who{position:absolute;left:72px;top:648px;width:1056px;height:284px;background:var(--card);border-radius:18px;border:1px solid #e3e5e8}
.avatar{position:absolute;left:28px;top:22px;width:240px;height:240px;border-radius:50%;background:linear-gradient(160deg,#d9dde3,#9aa7b6);border:6px solid var(--white)}
.who-body{position:absolute;left:300px;top:28px;width:720px}
.title{color:var(--blue);font-weight:800;font-size:34px;letter-spacing:1px}
.who .title{text-align:center;margin-right:120px}
.copy{font-size:15px;line-height:24px;margin-top:14px}
.btn{display:inline-block;background:var(--blue);color:var(--white);font-size:14px;font-weight:700;padding:9px 22px;border-radius:18px;margin-top:16px;letter-spacing:.5px}
.what{position:absolute;left:72px;top:960px;width:600px}
.what-img{position:absolute;left:708px;top:976px;width:420px;height:244px;border-radius:14px;background:linear-gradient(135deg,#cfd9e6,#6f8fb5 60%,#3c4e66)}
.band{position:absolute;left:0;width:1200px;background:var(--band)}
.center-title{text-align:center}
.grown-item{position:absolute;top:1372px;display:flex;gap:22px}
.grown-img{width:188px;height:160px;border-radius:10px}
.grown-item h3{font-size:22px;font-weight:800;color:var(--ink);margin-top:6px}
.grown-item .copy{width:230px;margin-top:8px}
.tiles{position:absolute;left:72px;top:1620px;display:flex;gap:24px}
.tile{width:246px;height:292px;background:var(--blue);border-radius:22px;color:var(--white);text-align:center;padding-top:48px}
.tile svg{width:92px;height:80px}
.tile h4{font-size:17px;font-weight:800;margin-top:28px;letter-spacing:.5px}
.tile p{font-size:14px;line-height:21px;margin:12px 26px 0;color:#e4ecf6}
.posts{position:absolute;left:72px;top:2068px;display:flex;gap:24px}
.post{width:336px}
.post-img{height:180px;border-radius:10px}
.post h5{font-size:19px;font-weight:800;color:var(--ink);margin-top:18px;line-height:24px}
.post .copy{margin-top:10px}
.more{display:block;color:var(--blue);font-size:14px;font-weight:700;margin-top:10px}
.footer{position:absolute;left:72px;top:2500px;width:1056px;display:flex;justify-content:space-between;font-size:14px;color:var(--muted)}
.follow{text-align:right;font-weight:700;color:var(--ink)}
.social{display:flex;gap:14px;margin-top:8px}
.social i{width:20px;height:20px;border-radius:50%;background:#8a8f96}
</style>
</head>
<body>
<header class="hero" role="img" aria-label="Photo of a climber on a rock face"></header>
<div class="topbar"><span class="brand">ARIN CASTELL</span><div class="burger"><span></span><span></span><span></span></div></div>
<div class="hero-copy"><h1>LOREM IPSUM DOLOR</h1><p>Vestibulum ante ipsum primis in faucibus orci luctus et ultrices posuere</p></div>
<div class="dots"><i></i><i></i><i class="on"></i><i></i></div>
<ul class="menu">
  <li>WHAT IS BRIGHT PATHWAY</li>
  <li>WHO I AM</li>
  <li>BACKGROUND - PROFESSIONAL</li>
  <li>BRAND MARKETING</li>
  <li>EMAIL AUTOMATION</li>
  <li>HIKING</li>
  <li>ROCK CLIMBING</li>
  <li>TRAVELING</li>
  <li><span>EXERCISING AND TRANSFORMATION<small>"Personal Thoughts"</small></span></li>
</ul>

<section class="who">
  <div class="avatar" role="img" aria-label="Portrait photo of the author"></div>
  <div class="who-body">
    <h2 class="title">WHO I AM</h2>
    <p class="copy">Aliquam molestie, mi et imperdiet euismod, dui purus auctor tellus, at interdum lacus tellus at ante. Sed accumsan sollicitudin sapien, sit amet adipiscing lorem gravida eu. In congue, neque ac lobortis volutpat, libero mauris varius mi, vitae suscipit ipsum ligula vitae risus. Duis aliquet nibh a dui mollis, in gravida est rhoncus. Vivamus egestas risus in magna commodo. Sed semper viverra sapien. Etiam pretium porttitor lectus, vel ornare neque porta volutpat.</p>
    <span class="btn">READ MORE</span>
  </div>
</section>

<section class="what">
  <h2 class="title">WHAT IS BRIGHT PATHWAY ?</h2>
  <p class="copy">Aliquam molestie, mi et imperdiet euismod, dui purus auctor tellus, at interdum lacus tellus at ante. Sed accumsan sollicitudin sapien, sit amet adipiscing lorem gravida eu. In congue, neque ac lobortis volutpat, libero mauris varius mi, vitae suscipit ipsum ligula vitae risus. Duis aliquet nibh a dui mollis, in gravida est rhoncus. Vivamus egestas risus in magna commodo.</p>
  <span class="btn">READ MORE</span>
</section>
<div class="what-img" role="img" aria-label="Photo of a team meeting around a presentation screen"></div>

<section class="band" style="top:1272px;height:296px">
  <h2 class="title center-title" style="margin-top:36px">HOW I HAVE GROWN</h2>
</section>
<div class="grown-item" style="left:72px">
  <div class="grown-img" role="img" aria-label="Photo of colleagues at work" style="background:linear-gradient(135deg,#e4e6ea,#8f9aa8)"></div>
  <div><h3>PROFESSIONAL</h3><p class="copy">Suspendisse lobortis turpis in odio tincidunt, eu interdum lorem euismod. Etiam risus massa, vulputate eu.</p><span class="btn">READ MORE</span></div>
</div>
<div class="grown-item" style="left:620px">
  <div class="grown-img" role="img" aria-label="Photo of a person thinking in front of a chalkboard" style="background:linear-gradient(135deg,#3a3f47,#15181d)"></div>
  <div><h3>PERSONAL THOUGHTS</h3><p class="copy">Suspendisse lobortis turpis in odio tincidunt, eu interdum lorem euismod. Etiam risus massa, vulputate eu.</p><span class="btn">READ MORE</span></div>
</div>

<section class="tiles">
  <article class="tile">
    <svg viewBox="0 0 92 80" fill="none" stroke="#fff" stroke-width="5"><rect x="16" y="8" width="60" height="42" rx="3"/><path d="M4 62h84l-6 10H10z" fill="#fff"/></svg>
    <h4>BRAND MARKETING</h4><p>Suspendisse lobortis turpis in odio tincidunt, eu interdum lorem euismod egestas risus in magna varius.</p>
  </article>
  <article class="tile">
    <svg viewBox="0 0 92 80"><rect x="6" y="12" width="80" height="56" rx="4" fill="#fff"/><path d="M8 16l38 30 38-30" fill="none" stroke="#2f6db5" stroke-width="5"/></svg>
    <h4>EMAIL AUTOMATION</h4><p>Suspendisse lobortis turpis in odio tincidunt, eu interdum lorem euismod egestas risus in magna varius.</p>
  </article>
  <article class="tile">
    <svg viewBox="0 0 92 80" fill="#fff"><path d="M40 4h10l4 28 30 14v8l-30-6-2 18 8 6v6l-14-4-14 4v-6l8-6-2-18-30 6v-8l30-14z"/></svg>
    <h4>TRAVELING</h4><p>Suspendisse lobortis turpis in odio tincidunt, eu interdum lorem euismod egestas risus in magna varius.</p>
  </article>
  <article class="tile">
    <svg viewBox="0 0 92 80" fill="#fff"><path d="M4 74l28-48 14 22 12-16 30 42z"/></svg>
    <h4>HIKING</h4><p>Suspendisse lobortis turpis in odio tincidunt, eu interdum lorem euismod egestas risus in magna varius.</p>
  </article>
</section>

<section class="band" style="top:1960px;height:520px">
  <h2 class="title center-title" style="margin-top:56px">BLOGS &amp; ARTICLES</h2>
</section>
<div class="posts">
  <article class="post"><div class="post-img" role="img" aria-label="Photo of people working together at a laptop" style="background:linear-gradient(135deg,#c9a27e,#6b4d38)"></div><h5>NAM FERMENTUM VESTIBULUM PURUS ID ALIQUET.</h5><p class="copy">Suspendisse lobortis turpis in odio tincidunt, eu interdum lorem euismod. Etiam risus massa, vulputate eu.</p><span class="more">Continue Reading</span></article>
  <article class="post"><div class="post-img" role="img" aria-label="Photo of a businessman in a bright city street" style="background:linear-gradient(135deg,#f0d7a6,#9a7c5c 55%,#4a4540)"></div><h5>NAM FERMENTUM VESTIBULUM PURUS ID ALIQUET.</h5><p class="copy">Suspendisse lobortis turpis in odio tincidunt, eu interdum lorem euismod. Etiam risus massa, vulputate eu.</p><span class="more">Continue Reading</span></article>
  <article class="post"><div class="post-img" role="img" aria-label="Photo of a desk with notebook and coffee" style="background:linear-gradient(135deg,#e9dccb,#b08f72)"></div><h5>NAM FERMENTUM VESTIBULUM PURUS ID ALIQUET.</h5><p class="copy">Suspendisse lobortis turpis in odio tincidunt, eu interdum lorem euismod. Etiam risus massa, vulputate eu.</p><span class="more">Continue Reading</span></article>
</div>

<footer class="footer">
  <p>Copyright © 2016 Company Name<br>All Rights Reserved</p>
  <div class="follow">FOLLOW ME<div class="social"><i></i><i></i><i></i><i></i><i></i><i></i></div></div>
</footer>
</body>
</html>
```